Updated Logo, New Marketing Brochure, & New Business Cards

Hello! I actually have a few things I need some assistance with. I want to make some minor tweaks to my current branding and logo design. I believe I have the vector file- but the previous graphic designer I worked with through gigrunn did not give me everything I paid for, and stopped responding to my messages. So, I don’t want to work with her again.

I also need new business cards using this branding change, as well as some brochures to handout to doctors offices and other businesses that I am marketing my teen counseling services to.

Here is my practice’s site to get an idea of my current branding
www.LanternSkye.com

I would love an idea on budget and timeframe! Thankyou so much.
-Marisol

Target Market(s)

Teen Girls needing Counseling Services

Industry/Entity Type

Counsellor

Requirements
Must have
• My current branding colors and logo design with some minor alterations. A fresh layout for brochures that draws interest, while quickly speaking to the needs of the parents and teen girls that I serve.

```html
<!DOCTYPE html>
<html lang="en">
<head>
<meta charset="utf-8">
<title>LanternSkye Flyer</title>
<link href="https://fonts.googleapis.com/css2?family=Pinyon+Script&family=Source+Sans+3:wght@400;600;700&display=swap" rel="stylesheet">
<style>
  :root {
    --stage: #a3a3a3;
    --teal-band: #0f7f79;
    --teal-bright: #19b3a6;
    --teal-logo: #137a74;
    --ink-dark: #121212;
    --white: #ffffff;
    --body-light: #e9e9e9;
  }
  * { margin: 0; padding: 0; box-sizing: border-box; }
  html, body { width: 1200px; height: 1200px; overflow: hidden; }
  body {
    background: var(--stage);
    font-family: "Source Sans 3", "Helvetica Neue", Arial, sans-serif;
    position: relative;
  }
  .flyer {
    position: absolute;
    left: 233px;
    width: 753px;
    height: 538px;
    overflow: hidden;
  }
  .flyer--front { top: 47px; background: #f1f1f1; }
  .flyer--back { top: 622px; background: var(--ink-dark); color: var(--white); }

  .front-photo {
    position: absolute; inset: 0;
    background: linear-gradient(180deg, #f4f4f4 0%, #ececec 28%, #b9a79a 52%, #6f7d96 72%, #3d4a63 100%);
  }
  .brand {
    position: absolute;
    left: 0; right: 0;
    text-align: center;
  }
  .brand__name {
    display: block;
    font-weight: 700;
    font-size: 40px;
    letter-spacing: 0.5px;
    line-height: 1;
  }
  .brand__tagline {
    display: block;
    font-size: 11px;
    margin-top: 6px;
  }
  .flyer--front .brand { top: 42px; color: var(--teal-logo); }
  .flyer--back .brand { top: 32px; color: var(--white); }

  .script-band {
    position: absolute;
    left: 0; right: 0;
    top: 428px; height: 61px;
    background: var(--teal-band);
    color: var(--white);
    font-family: "Pinyon Script", cursive;
    font-size: 34px;
    display: flex; align-items: center; justify-content: center;
  }

  .script-heading {
    position: absolute;
    top: 112px; left: 0; right: 0;
    text-align: center;
    font-family: "Pinyon Script", cursive;
    font-size: 30px;
  }
  .service {
    position: absolute;
    width: 304px;
  }
  .service__title {
    color: var(--teal-bright);
    font-weight: 700;
    font-size: 18px;
    line-height: 1.1;
    position: relative;
    padding-left: 20px;
  }
  .service__title::before {
    content: "";
    position: absolute;
    left: 0; top: 5px;
    width: 10px; height: 10px;
    border-radius: 50%;
    background: #d9efe9;
  }
  .service__text {
    padding-left: 20px;
    font-size: 11.4px;
    line-height: 14.5px;
    color: var(--body-light);
    text-align: justify;
    margin-top: 1px;
  }
  .service--anxiety { left: 46px; top: 178px; }
  .service--depression { left: 46px; top: 268px; }
  .service--transitions { left: 403px; top: 178px; }
  .service--teen { left: 403px; top: 281px; }

  .cta-band {
    position: absolute;
    left: 0; right: 0;
    top: 399px; height: 52px;
    background: var(--teal-band);
    padding: 7px 46px;
    font-weight: 600;
    font-size: 14.6px;
    line-height: 18.5px;
  }
  .call {
    position: absolute;
    top: 464px; left: 0; right: 0;
    text-align: center;
    font-weight: 600;
    font-size: 18px;
  }
  .social {
    position: absolute;
    top: 493px; left: 348px;
    display: flex; gap: 13px;
  }
  .social__tile {
    width: 24px; height: 24px;
    background: var(--teal-band);
    border-radius: 2px;
  }
</style>
</head>
<body>

<section class="flyer flyer--front">
  <div class="front-photo" role="img" aria-label="Group photo of eight smiling women of different ages standing in front of a white brick wall"></div>
  <div class="brand">
    <span class="brand__name">LanternSkye</span>
    <span class="brand__tagline">Support for Women and Teenage Girls</span>
  </div>
  <div class="script-band">Support and Counseling for Women and Teen Girls</div>
</section>

<section class="flyer flyer--back">
  <div class="brand">
    <span class="brand__name">LanternSkye</span>
    <span class="brand__tagline">Support for Women and Teenage Girls</span>
  </div>
  <h2 class="script-heading">Support and Counseling for Women and Teen Girls</h2>

  <article class="service service--anxiety">
    <h3 class="service__title">Anxiety</h3>
    <p class="service__text">LanternSkye, LLC can help you not only learn skills to better manage these symptoms, but also overcome those troublesome thoughts and worries that are disrupting your life.</p>
  </article>

  <article class="service service--depression">
    <h3 class="service__title">Depression</h3>
    <p class="service__text">LanternSkye, LLC is all about meeting a person exactly where they are at and then inviting them into a different way to do life. There is no magic wand to immediately alleviate suffering, but there are tools and help that LanternSkye, LLC can provide to help you manage and overcome these struggles.</p>
  </article>

  <article class="service service--transitions">
    <h3 class="service__title">Life Transitions</h3>
    <p class="service__text">It is inside these messy transitions of life that our boat feels so rocked or flipped over; we begin to lose sight of what's up and what's down. It's so normal to feel lost and uncertain on where to go next.</p>
  </article>

  <article class="service service--teen">
    <h3 class="service__title">Teen Girl Counseling</h3>
    <p class="service__text">Because teens are growing up in a generation of instant gratification- where they are glued to their phones and decisions are driven by social media norms- their awareness tends to focus on their external world, leading to a lack of good insight and self-awareness.</p>
  </article>

  <div class="cta-band">LanternSkye is here to help you reconnect with yourself inside of this life transition. Contact me today to take the next step towards learning to manage this transition more effectively.</div>

  <p class="call">Call Us today : 615-555-0142</p>
  <div class="social" aria-label="Social media links">
    <span class="social__tile"></span>
    <span class="social__tile"></span>
    <span class="social__tile"></span>
  </div>
</section>

</body>
</html>
```